Brisk Lantern Business Card

We need a business card design for an existing company (www.brisk-lantern.com). The business cards will be by Tavi in their Orra range (http://uk.tavi-print.example/products/orra/business-cards.html).

The card should be landscape, with the full company logo on the reverse side. I would like to have the card to portray a professional image (this is a high technology niche consultancy company). The card should be mostly white but aligned with our website (this is mostly dark colours). I can supply the logo files etc.

Details on the card should include the following:

Name (example: Gordon Pemberly)
Position (example: Principal Consultant)
Email Address (example: gordon@brisk-lantern.com)
Mobile Phone Number (example: +44 (0) 7519 804 372)
Website (example: www.brisk-lantern.com)
Flitter (example: @brisklanternco)
Gatherly (example: www.facebook.com/brisklanternco)

I would like the text on the front of the card to be black. Thanks.

Requirements
Should not have
• The company address on the card.

```html
<!DOCTYPE html>
<html lang="en">
<head>
<meta charset="utf-8">
<title>Brisk Lantern – Business Card</title>
<link rel="stylesheet" href="https://fonts.googleapis.com/css2?family=Varela+Round&display=swap">
<style>
  :root {
    --card-bg: #ffffff;
    --ink: #4a4a4a;
    --accent: #f47c20;
    --accent-soft: #fdeee2;
    --wash: #fbf4ee;
    --shadow: #f0f0f0;
  }
  html, body {
    margin: 0;
    padding: 0;
    width: 1200px;
    height: 686px;
    overflow: hidden;
    background: var(--card-bg);
  }
  .card {
    position: relative;
    width: 1200px;
    height: 686px;
    background: var(--card-bg);
    font-family: "Varela Round", Arial, sans-serif;
    color: var(--ink);
  }
  .backdrop {
    position: absolute;
    left: 0;
    top: 0;
  }
  .brand {
    position: absolute;
    left: 0;
    right: 0;
    top: 128px;
    display: flex;
    justify-content: center;
    align-items: center;
    gap: 12px;
  }
  .brand-dot {
    width: 26px;
    height: 26px;
    border-radius: 50%;
    background: var(--accent);
  }
  .brand-name {
    font-size: 30px;
    color: var(--accent);
    letter-spacing: 0.5px;
  }
  .identity {
    position: absolute;
    left: 0;
    right: 0;
    top: 220px;
    text-align: center;
  }
  .person-name {
    margin: 0;
    font-size: 50px;
    font-weight: 700;
    letter-spacing: 1px;
    word-spacing: 10px;
    color: var(--ink);
    -webkit-text-stroke: 0.8px var(--ink);
  }
  .person-role {
    margin: 12px 0 0;
    font-size: 27px;
    letter-spacing: 1.5px;
    color: var(--accent);
    -webkit-text-stroke: 0.3px var(--accent);
  }
  .contact {
    position: absolute;
    top: 443px;
    margin: 0;
    padding: 0;
    list-style: none;
    font-size: 21px;
    line-height: 38.5px;
    word-spacing: 4px;
    -webkit-text-stroke: 0.3px currentColor;
  }
  .contact-main {
    left: 209px;
    color: var(--ink);
  }
  .contact-social {
    right: 210px;
    text-align: right;
    color: var(--accent);
  }
</style>
</head>
<body>
  <main class="card">
    <svg class="backdrop" width="1200" height="686" viewBox="0 0 1200 686" role="img" aria-label="Faint soft wash behind the card details where the company mark appears as a large decoration">
      <defs>
        <radialGradient id="wash" cx="50%" cy="50%" r="50%">
          <stop offset="0%" stop-color="#fbf4ee" stop-opacity="1"/>
          <stop offset="70%" stop-color="#fdeee2" stop-opacity="0.6"/>
          <stop offset="100%" stop-color="#ffffff" stop-opacity="0"/>
        </radialGradient>
      </defs>
      <rect x="130" y="40" width="940" height="540" fill="url(#wash)"/>
      <ellipse class="floor-shadow" cx="604" cy="671" rx="160" ry="17" fill="#f0f0f0"/>
    </svg>

    <div class="brand">
      <span class="brand-dot"></span>
      <span class="brand-name">Brisk Lantern</span>
    </div>

    <header class="identity">
      <h1 class="person-name">Gordon Pemberly</h1>
      <p class="person-role">PRINCIPAL CONSULTANT</p>
    </header>

    <ul class="contact contact-main">
      <li>gordon@brisk-lantern.com</li>
      <li>+44 (0) 7519 804 372</li>
      <li>www.brisk-lantern.com</li>
    </ul>

    <ul class="contact contact-social">
      <li>Flitter: @brisklanternco</li>
      <li>Gatherly: brisklanternco</li>
    </ul>
  </main>
</body>
</html>
```